Redesign of the UI of a customer service platform

To improve the user experience of our customers, we need a new design for our agent interface of our customer service platform (quillvane.com).
The focus will be on the dashboard and the inbox screens (see attached) along with the common UI elements (Buttons, menu, fonts, forms...)
We want a simple and distinctive design

Target Market(s)

Worldwide

Industry/Entity Type

It Service

Number of Pages Required

3 page

Font styles to use
Sans Serif

Requirements
Must have
• New Onboarding page: this is a new page that is shown to user the first time they login to the platform. This will replace the current onboarding screen (setup SMS, Setup widget...etc)
• Dashboard page: to access important information and activate services (see screenshot from current site)
• Inbox page: to manage all the interactions with customers. (see screenshot from current site)
• UI elements (buttons, menus, forms, tables, fonts, color palette)

```html
<!DOCTYPE html>
<html lang="en">
<head>
<meta charset="utf-8">
<title>Quillvane – Agent Dashboard</title>
<link rel="stylesheet" href="https://fonts.googleapis.com/css2?family=Raleway:wght@300;400;500&family=Roboto:wght@300;400;500&display=swap">
<style>
:root{
  --orange:#f26b3a;
  --orange-soft:#f8a04b;
  --dark:#3a3f44;
  --dark-2:#2f3439;
  --side-text:#a9aeb3;
  --green:#1fbf5a;
  --green-dark:#128a45;
  --blue:#1680d6;
  --red:#d7304f;
  --slate:#3e4b60;
  --panel:#e8ebef;
  --ink:#2f3337;
  --muted:#7b8087;
  --grid:#e3e5e8;
  --pink:#f2a9b4;
  --purple:#9a3bc6;
}
*{box-sizing:border-box;margin:0;padding:0}
html,body{width:1200px;height:674px;overflow:hidden;background:#fff}
.stage{position:relative;width:1500px;height:843px;transform:scale(.8);transform-origin:0 0;font-family:"Roboto",sans-serif;color:var(--ink)}
.abs{position:absolute}

/* top bar */
.topbar{position:absolute;left:0;top:0;width:1500px;height:46px;background:var(--dark);border-bottom:4px solid var(--orange)}
.topbar .item{position:absolute;top:13px;color:#e9ecef;font-size:14px;letter-spacing:.5px}
.badge{position:absolute;width:15px;height:15px;border-radius:50%;background:var(--orange);color:#fff;font-size:9px;line-height:15px;text-align:center}

/* sidebar */
.sidebar{position:absolute;left:0;top:46px;width:158px;height:797px;background:var(--dark);border-right:4px solid var(--orange)}
.nav-item{position:absolute;left:0;width:154px;text-align:center;color:var(--side-text);font-size:13px}
.nav-item svg{display:block;margin:0 auto 6px}
.nav-item.active{background:var(--orange);color:#fff;top:4px;height:97px;padding-top:25px}
.nav-badge{position:absolute;left:111px;width:23px;height:23px;border-radius:50%;background:#fff;color:var(--dark);font-size:14px;line-height:23px;text-align:center}

h1.title{position:absolute;left:212px;top:62px;font-family:"Raleway",sans-serif;font-weight:300;font-size:48px;letter-spacing:1.5px;color:var(--ink)}

.alert{position:absolute;left:939px;top:54px;width:205px;height:31px;border:1px solid #e06a7a;background:#fdf2f3;color:#d7304f;font-size:12px;display:flex;align-items:center;gap:10px;padding-left:12px}
.alert .dot{width:17px;height:17px;border-radius:50%;background:var(--red);color:#fff;font-weight:500;font-size:12px;line-height:17px;text-align:center}

.panel-head{position:absolute;background:var(--panel);color:#4a4f55;font-family:"Raleway",sans-serif;font-size:13px;letter-spacing:.3px;padding-left:24px;display:flex;align-items:center}
.panel-head.orange{background:var(--orange);color:#fff;font-size:14px}

/* conversations */
.convo-name{position:absolute;font-family:"Raleway",sans-serif;font-size:16px;letter-spacing:2.5px;color:var(--ink)}
.convo-line{position:absolute;font-size:10px;color:#3d4146}
.convo-task{position:absolute;font-size:12.5px;color:#4a4f55;line-height:12px}
.avatar{position:absolute;border-radius:50%}

/* calendar */
.cal-head{position:absolute;left:579px;top:166px;width:293px;font-family:"Raleway",sans-serif;font-size:16px;letter-spacing:.5px;text-align:center}
.cal-day{position:absolute;font-size:11px;width:36px;text-align:center;color:var(--ink)}
.cal-day.wk{font-size:9.5px;color:#3d4146}
.cal-day.off{color:#c2c5c9}
.cal-band{position:absolute;height:26px;background:#c9cbce;border-radius:13px}
.cal-dot{position:absolute;width:28px;height:28px;border-radius:50%;background:var(--orange-soft);color:#fff;font-size:11px;line-height:28px;text-align:center}

.legend{position:absolute;font-size:11px;color:#4a4f55;display:flex;align-items:center;gap:6px}
.legend i{width:7px;height:7px;border-radius:50%;display:inline-block}

.stat-num{position:absolute;font-family:"Raleway",sans-serif;font-size:19px;color:#3d4146}
.stat-cap{position:absolute;font-size:8.5px;letter-spacing:.6px;color:#4a4f55}
.plat-num{position:absolute;font-size:14px;color:#3d4146}
</style>
</head>
<body>
<div class="stage">

  <!-- Top bar -->
  <header class="topbar">
    <svg class="abs" style="left:69px;top:14px" width="20" height="16" viewBox="0 0 20 16"><g fill="#c9cdd1"><rect y="0" width="20" height="2"/><rect y="5" width="20" height="2"/><rect y="10" width="20" height="2"/><rect y="14" width="20" height="2"/></g></svg>
    <svg class="abs" style="left:950px;top:15px" width="16" height="14" viewBox="0 0 16 14"><g fill="#e9ecef"><rect width="2" height="2"/><rect x="4" width="12" height="2"/><rect y="4" width="2" height="2"/><rect x="4" y="4" width="12" height="2"/><rect y="8" width="2" height="2"/><rect x="4" y="8" width="12" height="2"/><rect y="12" width="2" height="2"/><rect x="4" y="12" width="12" height="2"/></g></svg>
    <span class="badge" style="left:961px;top:26px">2</span>
    <svg class="abs" style="left:1029px;top:15px" width="20" height="14" viewBox="0 0 20 14"><path d="M3 0h14l3 6v8H0V6z" fill="#e9ecef"/><path d="M2 6h5l1 2h4l1-2h5" fill="none" stroke="#3a3f44" stroke-width="1.4"/></svg>
    <span class="badge" style="left:1046px;top:26px">4</span>
    <span class="abs" style="left:1111px;top:14px;width:16px;height:16px;border-radius:50%;background:var(--green)"></span>
    <span class="item" style="left:1142px">Availability</span>
    <svg class="abs" style="left:1228px;top:19px" width="11" height="7" viewBox="0 0 11 7"><path d="M1 1l4.5 4.5L10 1" fill="none" stroke="#e9ecef" stroke-width="1.6"/></svg>
    <svg class="abs" style="left:1296px;top:7px" width="31" height="31" viewBox="0 0 31 31" role="img" aria-label="User avatar"><circle cx="15.5" cy="15.5" r="15.5" fill="#fff"/><circle cx="15.5" cy="12" r="5.5" fill="#3a3f44"/><path d="M5 26c2-6 19-6 21 0" fill="#3a3f44"/></svg>
    <span class="item" style="left:1341px">User 1</span>
    <svg class="abs" style="left:1395px;top:19px" width="11" height="7" viewBox="0 0 11 7"><path d="M1 1l4.5 4.5L10 1" fill="none" stroke="#e9ecef" stroke-width="1.6"/></svg>
    <span class="abs" style="left:1464px;top:16px;width:13px;height:13px;border-radius:50%;background:#6f757b;color:var(--dark);font-size:10px;font-weight:500;line-height:13px;text-align:center">?</span>
  </header>

  <!-- Sidebar -->
  <nav class="sidebar">
    <div class="nav-item active">
      <svg width="30" height="30" viewBox="0 0 30 30"><circle cx="15" cy="12" r="9" fill="none" stroke="#fff" stroke-width="2.5"/><path d="M5 28c2-7 18-7 20 0z" fill="#fff"/><rect x="3" y="10" width="4" height="7" rx="1.5" fill="#fff"/><rect x="23" y="10" width="4" height="7" rx="1.5" fill="#fff"/></svg>
      Dashboard
    </div>
    <div class="nav-item" style="top:130px">
      <svg width="28" height="18" viewBox="0 0 28 18"><path d="M4 0h20l4 7v11H0V7z" fill="#a9aeb3"/><path d="M2 7h7l1.5 3h7L19 7h7" fill="none" stroke="#3a3f44" stroke-width="1.5"/></svg>
      Inbox
    </div>
    <span class="nav-badge" style="top:117px">4</span>
    <div class="nav-item" style="top:231px">
      <svg width="20" height="17" viewBox="0 0 20 17"><g fill="#a9aeb3"><rect width="3" height="2.4"/><rect x="5" width="15" height="2.4"/><rect y="5" width="3" height="2.4"/><rect x="5" y="5" width="15" height="2.4"/><rect y="10" width="3" height="2.4"/><rect x="5" y="10" width="15" height="2.4"/><rect y="14.6" width="3" height="2.4"/><rect x="5" y="14.6" width="15" height="2.4"/></g></svg>
      Tasks
    </div>
    <span class="nav-badge" style="top:216px">2</span>
    <div class="nav-item" style="top:328px">
      <svg width="20" height="20" viewBox="0 0 20 20"><circle cx="10" cy="6" r="5" fill="#a9aeb3"/><path d="M1 20c1-8 17-8 18 0z" fill="#a9aeb3"/></svg>
      Customers
    </div>
    <div class="nav-item" style="top:428px">
      <svg width="22" height="20" viewBox="0 0 22 20"><path d="M0 0l22 10L0 20l3-10z" fill="#a9aeb3"/><path d="M3 10h10" stroke="#3a3f44" stroke-width="1.5"/></svg>
      Campaigns
    </div>
    <div class="nav-item" style="top:524px">
      <svg width="14" height="22" viewBox="0 0 14 22"><text x="7" y="19" text-anchor="middle" font-family="Roboto,sans-serif" font-size="22" fill="#a9aeb3">$</text></svg>
      Payments
    </div>
    <div class="nav-item" style="top:628px">
      <svg width="19" height="17" viewBox="0 0 19 17"><g fill="#a9aeb3"><rect x="0" y="6" width="3" height="11"/><rect x="5" y="2" width="3" height="15"/><rect x="10" y="0" width="3" height="17"/><rect x="15" y="4" width="3" height="13"/></g></svg>
      Reports
    </div>
    <div class="nav-item" style="top:726px">
      <svg width="20" height="20" viewBox="0 0 20 20"><g fill="#a9aeb3"><circle cx="10" cy="10" r="7"/><rect x="8.5" y="0" width="3" height="20"/><rect x="0" y="8.5" width="20" height="3"/><rect x="8.5" y="0" width="3" height="20" transform="rotate(45 10 10)"/><rect x="8.5" y="0" width="3" height="20" transform="rotate(-45 10 10)"/></g><circle cx="10" cy="10" r="3" fill="#3a3f44"/></svg>
      Settings
    </div>
  </nav>

  <h1 class="title">Dashboard</h1>

  <div class="alert"><span class="dot">!</span>Important tast assigned.<span style="font-size:15px;margin-left:4px">✕</span></div>
  <svg class="abs" style="left:952px;top:46px" width="14" height="9" viewBox="0 0 14 9"><path d="M0 9L7 0l7 9" fill="#fdf2f3" stroke="#e06a7a"/></svg>

  <!-- Recent conversations -->
  <div class="panel-head orange" style="left:204px;top:150px;width:321px;height:50px">RECENT CONVERSATIONS</div>
  <span class="abs" style="left:517px;top:206px;width:2px;height:82px;background:#d3d6da"></span>

  <div class="avatar" role="img" aria-label="Portrait of Emma Argosto" style="left:226px;top:213px;width:60px;height:60px;background:radial-gradient(circle at 50% 45%,#f4d6a6,#e9c27a 55%,#f1f1f1 75%)"></div>
  <div class="convo-name" style="left:322px;top:209px">Emma Argosto</div>
  <svg class="abs" style="left:300px;top:236px" width="12" height="12" viewBox="0 0 12 12"><path d="M0 5L12 0 7 12 5.5 6.5z" fill="#e8533a"/></svg>
  <div class="convo-line" style="left:321px;top:237px">Yes that would be great, please do t...</div>
  <svg class="abs" style="left:302px;top:255px" width="10" height="10" viewBox="0 0 10 10"><circle cx="5" cy="5" r="4" fill="none" stroke="#4a4f55" stroke-width="1.3"/><path d="M5 2.5V5h2" fill="none" stroke="#4a4f55" stroke-width="1.2"/></svg>
  <div class="convo-task" style="left:321px;top:256px">Check if customer was billed<br>twice</div>

  <svg class="abs" style="left:231px;top:305px" width="48" height="48" viewBox="0 0 48 48" role="img" aria-label="Default avatar for Lawrence Mathes"><circle cx="24" cy="16" r="11" fill="#3d4a5e"/><path d="M3 46c3-17 39-17 42 0z" fill="#3d4a5e"/></svg>
  <div class="convo-name" style="left:331px;top:295px">Lawrence Mathes</div>
  <span class="abs" style="left:300px;top:322px;width:12px;height:12px;border-radius:50%;background:var(--blue)"></span>
  <div class="convo-line" style="left:321px;top:323px;color:var(--blue)">So how soon can this be done?</div>
  <svg class="abs" style="left:302px;top:341px" width="10" height="10" viewBox="0 0 10 10"><circle cx="5" cy="5" r="4" fill="none" stroke="#4a4f55" stroke-width="1.3"/><path d="M5 2.5V5h2" fill="none" stroke="#4a4f55" stroke-width="1.2"/></svg>
  <div class="convo-task" style="left:321px;top:342px">Verify account and banking<br>details</div>

  <div class="avatar" role="img" aria-label="Portrait of Melvin B. Banks" style="left:225px;top:384px;width:60px;height:60px;background:radial-gradient(circle at 50% 40%,#5a3a2a,#7a4a3a 45%,#d9678f 70%,#6fb3d2)"></div>
  <div class="convo-name" style="left:323px;top:381px">Melvin B. Banks</div>
  <svg class="abs" style="left:300px;top:408px" width="12" height="11" viewBox="0 0 12 11"><rect x="1" y="1" width="10" height="7" fill="none" stroke="#4a4f55" stroke-width="1.2"/><path d="M0 10h12" stroke="#4a4f55" stroke-width="1.2"/></svg>
  <div class="convo-line" style="left:321px;top:409px">Hi, I was just wandering how quickly...</div>
  <svg class="abs" style="left:302px;top:427px" width="10" height="10" viewBox="0 0 10 10"><circle cx="5" cy="5" r="4" fill="none" stroke="#4a4f55" stroke-width="1.3"/><path d="M5 2.5V5h2" fill="none" stroke="#4a4f55" stroke-width="1.2"/></svg>
  <div class="convo-task" style="left:321px;top:428px">Check delivery times</div>

  <!-- Calendar -->
  <svg class="abs" style="left:601px;top:170px" width="15" height="12" viewBox="0 0 15 12"><path d="M14 6H2M6 1L1 6l5 5" fill="none" stroke="#2f3337" stroke-width="1.6"/></svg>
  <div class="cal-head">FEBRUARY 2015</div>
  <svg class="abs" style="left:835px;top:170px" width="15" height="12" viewBox="0 0 15 12"><path d="M1 6h12M9 1l5 5-5 5" fill="none" stroke="#2f3337" stroke-width="1.6"/></svg>
  <span class="abs" style="left:579px;top:204px;width:293px;height:1px;background:#cfd2d6"></span>
  <span class="abs" style="left:579px;top:228px;width:293px;height:1px;background:#eceef0"></span>

  <div class="cal-day wk" style="left:594px;top:211px">MON</div>
  <div class="cal-day wk" style="left:632px;top:211px">TUE</div>
  <div class="cal-day wk" style="left:670px;top:211px">WED</div>
  <div class="cal-day wk" style="left:708px;top:211px">THU</div>
  <div class="cal-day wk" style="left:746px;top:211px">FRI</div>
  <div class="cal-day wk" style="left:784px;top:211px">SAT</div>
  <div class="cal-day wk" style="left:821px;top:211px">SUN</div>

  <div class="cal-day off" style="left:594px;top:257px">26</div>
  <div class="cal-day off" style="left:632px;top:257px">27</div>
  <div class="cal-day off" style="left:670px;top:257px">28</div>
  <div class="cal-day off" style="left:708px;top:257px">29</div>
  <div class="cal-day off" style="left:746px;top:257px">30</div>
  <div class="cal-day off" style="left:784px;top:257px">31</div>
  <div class="cal-day" style="left:821px;top:257px">1</div>

  <span class="cal-band" style="left:790px;top:290px;width:78px;background:linear-gradient(90deg,#c9cbce 70%,rgba(201,203,206,0))"></span>
  <div class="cal-day" style="left:594px;top:297px">2</div>
  <div class="cal-day" style="left:632px;top:297px">3</div>
  <div class="cal-day" style="left:670px;top:297px">4</div>
  <div class="cal-day" style="left:708px;top:297px">5</div>
  <div class="cal-day" style="left:746px;top:297px">6</div>
  <div class="cal-dot" style="left:788px;top:289px">7</div>
  <div class="cal-day" style="left:821px;top:297px">8</div>

  <span class="cal-band" style="left:583px;top:329px;width:157px;background:linear-gradient(90deg,rgba(201,203,206,0),#c9cbce 14%)"></span>
  <div class="cal-day" style="left:594px;top:336px">9</div>
  <div class="cal-day" style="left:632px;top:336px">10</div>
  <div class="cal-day" style="left:670px;top:336px">11</div>
  <div class="cal-dot" style="left:712px;top:328px">12</div>
  <div class="cal-day" style="left:746px;top:336px">13</div>
  <div class="cal-day" style="left:784px;top:336px">14</div>
  <div class="cal-day" style="left:821px;top:336px">15</div>

  <div class="cal-day" style="left:594px;top:376px">16</div>
  <div class="cal-day" style="left:632px;top:376px">17</div>
  <div class="cal-day" style="left:670px;top:376px">18</div>
  <div class="cal-day" style="left:708px;top:376px">19</div>
  <div class="cal-day" style="left:746px;top:376px">20</div>
  <div class="cal-day" style="left:784px;top:376px">21</div>
  <div class="cal-day" style="left:821px;top:376px">22</div>

  <div class="cal-day" style="left:594px;top:415px">23</div>
  <div class="cal-day" style="left:632px;top:415px">24</div>
  <div class="cal-day" style="left:670px;top:415px">25</div>
  <div class="cal-day" style="left:708px;top:415px">26</div>
  <div class="cal-day" style="left:746px;top:415px">27</div>
  <div class="cal-day" style="left:784px;top:415px">28</div>
  <div class="cal-day off" style="left:821px;top:415px">1</div>

  <!-- Conversation statistics -->
  <div class="panel-head" style="left:925px;top:150px;width:292px;height:55px">CONVERSATIONS STATISTICS</div>
  <div class="legend" style="left:934px;top:226px"><i style="background:var(--green)"></i>Successful</div>
  <div class="legend" style="left:1034px;top:226px"><i style="background:var(--blue)"></i>Transfered</div>
  <div class="legend" style="left:1131px;top:226px"><i style="background:var(--red)"></i>Unsuccessful</div>
  <svg class="abs" style="left:940px;top:250px" width="260" height="210" viewBox="940 250 260 210" font-family="Roboto,sans-serif" font-size="9" fill="#6b7076">
    <g stroke="#dfe2e6" stroke-dasharray="2 3"><path d="M980 260H1190M980 288H1190M980 316H1190M980 344H1190M980 371H1190M980 399H1190"/></g>
    <path d="M980 427H1190" stroke="#dfe2e6"/>
    <g text-anchor="end"><text x="967" y="263">60</text><text x="967" y="291">50</text><text x="967" y="319">40</text><text x="967" y="347">30</text><text x="967" y="374">20</text><text x="967" y="402">10</text><text x="967" y="430">0</text></g>
    <g fill="var(--green)"><rect x="982" y="317" width="19" height="87"/><rect x="1014" y="290" width="19" height="87"/><rect x="1045" y="300" width="19" height="79"/><rect x="1077" y="317" width="19" height="64"/><rect x="1109" y="266" width="19" height="113"/><rect x="1140" y="307" width="19" height="92"/><rect x="1172" y="309" width="19" height="103"/></g>
    <g fill="var(--blue)"><rect x="982" y="404" width="19" height="16"/><rect x="1014" y="377" width="19" height="36"/><rect x="1045" y="379" width="19" height="24"/><rect x="1077" y="381" width="19" height="33"/><rect x="1109" y="379" width="19" height="28"/><rect x="1140" y="399" width="19" height="19"/><rect x="1172" y="412" width="19" height="11"/></g>
    <g fill="var(--red)"><rect x="982" y="420" width="19" height="7"/><rect x="1014" y="413" width="19" height="14"/><rect x="1045" y="403" width="19" height="24"/><rect x="1077" y="414" width="19" height="13"/><rect x="1109" y="407" width="19" height="20"/><rect x="1140" y="418" width="19" height="9"/><rect x="1172" y="423" width="19" height="4"/></g>
    <g text-anchor="middle"><text x="991" y="451">Mon</text><text x="1023" y="451">Tue</text><text x="1055" y="451">Wed</text><text x="1086" y="451">Thu</text><text x="1118" y="451">Fri</text><text x="1150" y="451">Sat</text><text x="1181" y="451">Sun</text></g>
  </svg>

  <!-- Right column stats -->
  <svg class="abs" style="left:1275px;top:170px" width="50" height="50" viewBox="0 0 50 50"><circle cx="25" cy="25" r="22" fill="none" stroke="#eceef0" stroke-width="3"/><circle cx="25" cy="25" r="22" fill="none" stroke="var(--orange-soft)" stroke-width="3" stroke-dasharray="103.7 138.2" transform="rotate(-90 25 25)"/><text x="25" y="29" text-anchor="middle" font-family="Roboto,sans-serif" font-size="11" fill="#4a4f55">75%</text></svg>
  <div class="stat-num" style="left:1337px;top:175px">15</div>
  <div class="stat-cap" style="left:1337px;top:201px">GOALS COMPLETED</div>

  <div class="stat-num" style="left:1285px;top:337px">535</div>
  <div class="stat-cap" style="left:1285px;top:363px">SESSIONS (LAST WEEK)</div>
  <svg class="abs" style="left:1412px;top:340px" width="40" height="32" viewBox="0 0 40 32"><g stroke-width="2"><path d="M2 32V18M7 32V12M12 32V6M17 32V14M22 32V2M27 32V16M32 32V20" stroke="var(--green)"/><path d="M37 32V14" stroke="var(--purple)"/></g></svg>

  <svg class="abs" style="left:1268px;top:512px" width="10" height="12" viewBox="0 0 10 12"><path d="M7 1L2 6l5 5" fill="none" stroke="#2f3337" stroke-width="1.5"/></svg>
  <span class="abs" style="left:1284px;top:480px;width:2px;height:76px;background:#f4c2b1"></span>
  <span class="abs" style="left:1448px;top:480px;width:2px;height:76px;background:#f4c2b1"></span>
  <svg class="abs" style="left:1360px;top:490px" width="22" height="20" viewBox="0 0 22 20"><circle cx="8" cy="5" r="4.5" fill="#3d4146"/><path d="M0 19c1-8 15-8 16 0z" fill="#3d4146"/><circle cx="16" cy="13" r="5" fill="#fff" stroke="#3d4146" stroke-width="1.5"/><path d="M16 10v6M13 13h6" stroke="#3d4146" stroke-width="1.5"/></svg>
  <div class="abs" style="left:1286px;top:517px;width:162px;text-align:center;font-size:12.5px;color:#2f3337">36 New Customers</div>
  <div class="abs" style="left:1286px;top:536px;width:170px;text-align:center;font-size:8.5px;color:var(--muted)">from 12 countries</div>
  <svg class="abs" style="left:1456px;top:512px" width="10" height="12" viewBox="0 0 10 12"><path d="M3 1l5 5-5 5" fill="none" stroke="#2f3337" stroke-width="1.5"/></svg>

  <svg class="abs" style="left:1286px;top:662px" width="10" height="12" viewBox="0 0 10 12"><path d="M7 1L2 6l5 5" fill="none" stroke="#2f3337" stroke-width="1.5"/></svg>
  <div class="abs" style="left:1300px;top:661px;width:144px;text-align:center;font-size:11.5px;letter-spacing:.4px;color:#3d4146">MARCH 2016</div>
  <svg class="abs" style="left:1444px;top:662px" width="10" height="12" viewBox="0 0 10 12"><path d="M3 1l5 5-5 5" fill="none" stroke="#2f3337" stroke-width="1.5"/></svg>
  <div class="abs" style="left:1290px;top:700px;width:70px;text-align:center;font-size:19px;color:#3d4146">1529</div>
  <div class="abs" style="left:1290px;top:726px;width:70px;text-align:center;font-size:8.5px;color:var(--muted)">New visitors</div>
  <span class="abs" style="left:1370px;top:700px;width:1px;height:38px;background:#dfe2e6"></span>
  <div class="abs" style="left:1378px;top:700px;width:80px;text-align:center;font-size:19px;color:#3d4146">473</div>
  <div class="abs" style="left:1378px;top:726px;width:80px;text-align:center;font-size:8.5px;color:var(--muted)">Repeated visitors</div>
  <svg class="abs" style="left:1288px;top:758px" width="166" height="36" viewBox="0 0 166 36"><g stroke="var(--pink)" stroke-width="1.6"><path d="M2 36V20M7 36V4M12 36V16M17 36V24M22 36V12M27 36V20M32 36V26M37 36V10M42 36V4M47 36V18M52 36V22M57 36V12M62 36V8M67 36V20M72 36V14M77 36V6M82 36V18M87 36V24M92 36V12M97 36V16M102 36V22M107 36V10M112 36V16M117 36V6M122 36V20M127 36V2M132 36V16M137 36V24M142 36V12M147 36V18M152 36V8M157 36V20M162 36V14"/></g></svg>

  <!-- Average payouts -->
  <div class="panel-head" style="left:315px;top:487px;width:343px;height:41px">AVERAGE PAYOUTS</div>
  <svg class="abs" style="left:325px;top:545px" width="325" height="215" viewBox="325 545 325 215" font-family="Roboto,sans-serif" font-size="6.5" fill="#8a8f95">
    <g stroke="#e6e8eb"><path d="M352 553H640M352 571H640M352 590H640M352 608H640M352 626H640M352 644H640M352 662H640M352 680H640M352 699H640M352 717H640M352 735H640"/></g>
    <g text-anchor="end"><text x="344" y="556">100</text><text x="344" y="574">90</text><text x="344" y="593">80</text><text x="344" y="611">70</text><text x="344" y="629">60</text><text x="344" y="647">50</text><text x="344" y="665">40</text><text x="344" y="683">30</text><text x="344" y="702">20</text><text x="344" y="720">10</text><text x="344" y="738">0</text></g>
    <path d="M485 612V735" stroke="#c7cbd0" stroke-dasharray="2 2"/>
    <polyline points="364,689 388,662 412,671 437,657 461,651 485,624 509,633 534,591 558,609 582,615 606,593 630,621" fill="none" stroke="var(--blue)" stroke-width="1.3"/>
    <g fill="#fff" stroke="var(--blue)" stroke-width="1.2"><circle cx="364" cy="689" r="2.6"/><circle cx="388" cy="662" r="2.6"/><circle cx="412" cy="671" r="2.6"/><circle cx="437" cy="657" r="2.6"/><circle cx="461" cy="651" r="2.6"/><circle cx="509" cy="633" r="2.6"/><circle cx="534" cy="591" r="2.6"/><circle cx="558" cy="609" r="2.6"/><circle cx="582" cy="615" r="2.6"/><circle cx="606" cy="593" r="2.6"/><circle cx="630" cy="621" r="2.6"/></g>
    <circle cx="485" cy="624" r="3" fill="var(--blue)"/>
    <rect x="459" y="595" width="52" height="17" rx="2" fill="#6c737b"/>
    <path d="M481 612l4 4 4-4z" fill="#6c737b"/>
    <text x="485" y="606" text-anchor="middle" fill="#fff" font-size="7.5">62 Payouts</text>
    <g text-anchor="middle"><text x="364" y="750">Jan</text><text x="388" y="750">Feb</text><text x="412" y="750">Mar</text><text x="437" y="750">Apr</text><text x="461" y="750">May</text><text x="485" y="750">Jun</text><text x="509" y="750">Jul</text><text x="534" y="750">Aug</text><text x="558" y="750">Sep</text><text x="582" y="750">Oct</text><text x="606" y="750">Nov</text><text x="630" y="750">Dec</text></g>
  </svg>
  <div class="legend" style="left:353px;top:777px;font-size:8.5px;color:var(--muted)"><i style="background:var(--blue);width:5px;height:5px"></i>Payouts</div>
  <div class="abs" style="left:556px;top:769px;width:85px;height:27px;border:1px solid #d5d8dc;border-radius:3px;background:#eef0f3;font-size:9px;color:var(--muted);padding:8px 0 0 9px">2016</div>
  <svg class="abs" style="left:623px;top:780px" width="8" height="5" viewBox="0 0 8 5"><path d="M1 1l3 3 3-3" fill="none" stroke="#6b7076" stroke-width="1.2"/></svg>

  <!-- Platforms used -->
  <div class="panel-head" style="left:797px;top:487px;width:296px;height:53px">PLATFORMS USED</div>
  <div class="legend" style="left:808px;top:547px;font-size:12px"><i style="background:var(--blue)"></i>Chatterly msg</div>
  <div class="legend" style="left:1029px;top:547px;font-size:12px">SMS<i style="background:var(--green-dark)"></i></div>
  <div class="plat-num" style="left:808px;top:569px">180</div>
  <div class="plat-num" style="left:1045px;top:569px">145</div>
  <svg class="abs" style="left:860px;top:580px" width="156" height="156" viewBox="860 580 156 156" font-family="Roboto,sans-serif">
    <g stroke="#fff" stroke-width="2">
      <path d="M937 586A72 72 0 0 1 1009 658L967 658A30 30 0 0 0 937 628Z" fill="var(--green-dark)"/>
      <path d="M1009 658A72 72 0 0 1 975.6 718.8L953.1 683.3A30 30 0 0 0 967 658Z" fill="var(--slate)"/>
      <path d="M975.6 718.8A72 72 0 0 1 870.1 684.5L909.1 669A30 30 0 0 0 953.1 683.3Z" fill="var(--orange)"/>
      <path d="M870.1 684.5A72 72 0 0 1 937 586L937 628A30 30 0 0 0 909.1 669Z" fill="var(--blue)"/>
    </g>
    <g fill="#fff" font-size="10.5" font-weight="500" text-anchor="middle"><text x="975" y="627">25%</text><text x="985" y="684">16%</text><text x="930" y="710">28%</text><text x="891" y="643">31%</text></g>
    <text x="938" y="657" text-anchor="middle" font-size="10.5" fill="#3d4146">580</text>
    <text x="938" y="669" text-anchor="middle" font-size="6" fill="#8a8f95">customers</text>
  </svg>
  <div class="plat-num" style="left:808px;top:730px">162</div>
  <div class="plat-num" style="left:1052px;top:730px">93</div>
  <div class="legend" style="left:808px;top:756px;font-size:12px"><i style="background:var(--orange)"></i>Wiremail</div>
  <div class="legend" style="left:1014px;top:756px;font-size:12px">Wigets<i style="background:var(--slate)"></i></div>

</div>
</body>
</html>
```